Web Design Project - Old Brackley (Bar)

We need a website for a new wine bar/hotel opening in Sydney's Kings Cross area. The concept is a rustic Australiana bar. We intend to use raw materials (sandstone, rusty metal etc) and lots of greenery/plants. It is set to be stylish and accessible to a young and middle age clientele.

The idea is to bring the outside inside.

The venue can cater for 450 people and is in one of the major nightclub strips in Australia. The demographic differs from celebrities to backpackers.

Target Market(s)

We are targeting 23yr - 40yr olds.

Industry/Entity Type

Hotel

Requirements
Must have
• What I want is a design to reflect is the fit out of the bar. We would like to see a rustic design to reflect the theme of the bar. The theme behind the fit out will be "bringing the outside inside" with lots of plants, wet walls etc.. There will be exposed brickwork, sandstone, timber and rusted steel with laser cut designs throughout the venue.
Nice to have
• I've attached some 3D designs that the venue will be roughly based on.

```html
<!DOCTYPE html>
<html lang="en">
<head>
<meta charset="utf-8">
<title>Old Brackley – Bar</title>
<link href="https://fonts.googleapis.com/css2?family=Cinzel:wght@400;700&family=Alegreya:wght@400;700&family=Open+Sans:wght@400;600;700&display=swap" rel="stylesheet">
<style>
:root{
  --wood-dark:#3a2314;
  --wood-mid:#5a3a22;
  --panel:#efe3cb;
  --panel-light:#f6ecd8;
  --cream:#f3e6cc;
  --ink:#2c1a10;
  --red:#8e1d16;
  --red-dark:#6e1410;
  --tan:#d8b98a;
  --nav:#2a170c;
  --text:#4a3526;
}
*{box-sizing:border-box;margin:0;padding:0}
html,body{width:793px;height:1200px;overflow:hidden}
body{
  font-family:"Open Sans",Arial,sans-serif;
  background:linear-gradient(180deg,var(--wood-mid),var(--wood-dark) 40%,#2e1b0f);
  color:var(--text);position:relative;
}
.site-header{
  position:absolute;left:0;top:0;width:793px;height:232px;
  background:linear-gradient(180deg,#8b6a4a 0%,#b89a78 45%,#9a7a58 100%);
}
.site-header::before{
  content:"";position:absolute;left:0;top:0;right:0;height:42px;
  background:linear-gradient(180deg,#4a2e1a,#6b4a30);
}
.brand{position:absolute;left:0;right:0;top:84px;text-align:center}
.brand-mark{display:inline-block;width:62px;height:62px;background:var(--ink);margin-bottom:8px}
.brand-name{font-family:"Cinzel",serif;font-size:21px;letter-spacing:2px;color:var(--ink);display:block}
.star{position:absolute;top:128px;width:26px;height:26px;fill:var(--red)}
.star.left{left:92px}.star.right{left:675px}
.main-nav{
  position:absolute;left:0;top:232px;width:793px;height:43px;
  background:linear-gradient(180deg,#3b2213,var(--nav));
  display:flex;justify-content:space-around;align-items:center;padding:0 30px;
  border-bottom:3px solid #1d0f07;
}
.main-nav a{color:#f0dcc0;font-size:13px;font-weight:600;text-decoration:none;letter-spacing:1px}
.main-nav a.active{color:#fff;font-weight:700}
.hero{position:absolute;left:26px;top:283px;width:741px;height:300px;background:var(--panel);}
.hero-photo{
  position:absolute;left:14px;top:28px;width:512px;height:256px;border:6px solid #fff;
  background:linear-gradient(135deg,#6b4a30,#a4704a 40%,#3c2618 75%,#5d4030);
  box-shadow:0 2px 6px rgba(0,0,0,.4);
}
.reservation{position:absolute;left:546px;top:12px;width:185px}
.reservation h2{font-size:14px;font-weight:700;color:var(--ink);margin-bottom:6px}
.reservation p{font-size:10.5px;line-height:1.38;margin-bottom:10px}
.phone{font-size:24px;font-weight:700;color:var(--red);letter-spacing:.5px;margin:4px 0 8px}
.btn{display:inline-block;background:var(--red-dark);color:#fff;font-family:"Alegreya",serif;font-size:15px;padding:8px 24px;border-radius:3px}
.gallery{
  position:absolute;left:0;top:590px;width:793px;height:128px;
  background:linear-gradient(180deg,#c9a577,#a98257);
  display:flex;align-items:center;justify-content:center;gap:10px;
}
.thumb{width:95px;height:104px;border:4px solid #fff;background:radial-gradient(circle at 50% 55%,#a35a2a,#6e7a2e 55%,#efe5d2 80%)}
.arrow{position:absolute;top:50px;width:14px;height:28px;fill:#fff}
.arrow.prev{left:6px}.arrow.next{right:6px}
.welcome{position:absolute;left:0;top:736px;width:793px;height:205px;background:var(--panel-light)}
.welcome h1{position:absolute;left:28px;top:10px;font-family:"Alegreya",serif;font-size:50px;font-weight:700;color:var(--ink)}
.welcome .rule{position:absolute;left:28px;top:76px;width:350px;height:1px;background:#b89a78}
.welcome .copy{position:absolute;left:28px;top:90px;width:350px;font-size:10.5px;line-height:1.45}
.welcome .copy p{margin-bottom:14px}
.wines{position:absolute;left:405px;top:46px;width:200px}
.wines h2{font-family:"Alegreya",serif;font-size:27px;color:var(--red);font-weight:700;margin-bottom:6px}
.wines p{font-size:10.5px;line-height:1.45;margin-bottom:10px}
.btn-small{display:inline-block;background:var(--tan);color:var(--ink);font-family:"Alegreya",serif;font-size:13px;font-weight:700;padding:4px 14px;border-radius:3px}
.wines-photo{position:absolute;left:622px;top:46px;width:158px;height:122px;background:linear-gradient(90deg,#1f140c,#5a1a16 40%,#2a1a10 70%,#c9b89a)}
.info-row{position:absolute;left:26px;top:958px;width:741px;display:flex;justify-content:space-between}
.info-card{width:232px;height:136px;background:var(--cream);border:3px solid #e9d8b6;border-radius:6px;text-align:center;padding-top:18px;box-shadow:0 2px 5px rgba(0,0,0,.35)}
.info-card h3{font-family:"Alegreya",serif;font-size:24px;font-weight:700;color:var(--ink);line-height:1}
.info-card .sub{font-size:10px;margin:6px 0 10px}
.info-card .big{font-family:"Alegreya",serif;font-size:20px;color:var(--red);font-weight:700}
.info-card .small{font-size:10.5px;line-height:1.4;padding:8px 20px 0}
.site-footer{position:absolute;left:0;top:1135px;width:793px;height:52px;background:#2a170c;display:flex;align-items:center;justify-content:space-between;padding:0 26px;color:#e6d3b6;font-size:11px}
.social{display:flex;gap:9px}
.social span{width:14px;height:14px;border-radius:50%;background:#e6d3b6}
</style>
</head>
<body>
<header class="site-header">
  <svg class="star left" viewBox="0 0 24 24"><path d="M12 1l3.2 7.2 7.8.7-5.9 5.2 1.8 7.7L12 17.8 5.1 21.8l1.8-7.7L1 8.9l7.8-.7z"/></svg>
  <svg class="star right" viewBox="0 0 24 24"><path d="M12 1l3.2 7.2 7.8.7-5.9 5.2 1.8 7.7L12 17.8 5.1 21.8l1.8-7.7L1 8.9l7.8-.7z"/></svg>
  <div class="brand"><span class="brand-mark"></span><span class="brand-name">OLD BRACKLEY</span></div>
</header>
<nav class="main-nav">
  <a class="active" href="#">HOME</a><a href="#">ABOUT US</a><a href="#">MENU</a><a href="#">RESERVATIONS</a><a href="#">LOCATION</a>
</nav>
<section class="hero">
  <div class="hero-photo" role="img" aria-label="Photo of the bar interior with brick walls, greenery and guests"></div>
  <div class="reservation">
    <h2>MAKE A RESERVATION!</h2>
    <p>I'm a Paragraph. Click here to add your own text and edit me. It's easy. Just click "Edit Text" or double click me and you can start adding your own content...</p>
    <p>Click here to make a reservation online or <b>call us</b></p>
    <div class="phone">1-800-555-0142</div>
    <span class="btn">Make a reservation</span>
  </div>
</section>
<section class="gallery">
  <svg class="arrow prev" viewBox="0 0 14 28"><path d="M12 2L2 14l10 12" stroke="#fff" stroke-width="3" fill="none"/></svg>
  <div class="thumb" role="img" aria-label="Steak dish"></div>
  <div class="thumb" role="img" aria-label="Grilled plate"></div>
  <div class="thumb" role="img" aria-label="Fresh salad"></div>
  <div class="thumb" role="img" aria-label="Main course"></div>
  <div class="thumb" role="img" aria-label="Steak dish"></div>
  <div class="thumb" role="img" aria-label="Grilled plate"></div>
  <div class="thumb" role="img" aria-label="Fresh salad"></div>
  <svg class="arrow next" viewBox="0 0 14 28"><path d="M2 2l10 12L2 26" stroke="#fff" stroke-width="3" fill="none"/></svg>
</section>
<section class="welcome">
  <h1>Welcome</h1>
  <div class="rule"></div>
  <div class="copy">
    <p>I'm a Paragraph. Click here to add your own text and edit me. It's easy. Just click "Edit Text" I'm a Paragraph.</p>
    <p>I'm a Paragraph. Click here to add your own text and edit me. It's easy. Just click "Edit Text" or double click me and you can start adding your own content...</p>
  </div>
  <div class="wines">
    <h2>Special Wines</h2>
    <p>We source the finest beers and wines and match them with your meal.</p>
    <span class="btn-small">READ MORE</span>
  </div>
  <div class="wines-photo" role="img" aria-label="Wine bottles and glass"></div>
</section>
<section class="info-row">
  <div class="info-card">
    <h3>WHERE ARE WE?</h3>
    <div class="sub">48 Laneway Rd, Sydney, AU 2011</div>
    <span class="btn-small">GET DIRECTIONS NOW</span>
  </div>
  <div class="info-card">
    <h3>OPENING HOURS</h3>
    <div class="sub">We're open everyday</div>
    <span class="btn-small big" style="background:var(--tan);color:var(--red)">12:00pm-1:00am</span>
  </div>
  <div class="info-card">
    <h3>CHEF AT HOME</h3>
    <div class="small">I'm a Paragraph. Click here to add your own text and edit me. It's easy. Just click "Edit Text"</div>
  </div>
</section>
<footer class="site-footer">
  <span>© 2013 by Old Brackley.</span>
  <div class="social"><span></span><span></span><span></span></div>
</footer>
</body>
</html>
```